Companybrochure for Consulting & Financing Firm

I need to have a Company Brochure asap for our company. We have a website that describes what we do, but we need also a brochure, that can be sent by PDF of eventually be printed as well.

The brochure should be short but nice and appealing to the customers.

We provide professional management consulting and help our customers to get finance for very diferent projects. Our business has a lot to do with personal relations, but also we are very professional in the way we work and how develop the solutions for our clients. Our clients are mainly government-owned firm, but also private trading companies and wealthy private investors.

Our customers are mainly in Latin America, but the company is headquater is in Switzerland. We are opening offices in Panama and Caracas, this should be easaly be adabtable later.

Please have a look at our website www.brevalto.ch. In the brochure, we would segment our services in 1.) Project Developments 2.) Management Conulting 3.) Investment Management and 4.) Finance Solutions.

Also do have a look at www.brevalto.ch
(Click E for the English version)

I managed to put the Mock-Up to the Website.
It is actually not really a mock-up, it is a version I have designed myself.
Well as I am not a designer, I hope you can make it much better.
The content however is what I would put in any other design as well.

Target Market(s)

Top Management, Investors, Entrepreneurs, Government Officials

Industry/Entity Type

Management Consulting

Requirements
Must have
• Design should reflect this image elements:

We are entrepreneurs.
We are comitted to get things done.
We work closely with the client side by side.
We are a professional partner.
We are not afraid of delivering unconventional solutions.
We look at the problem from various angles.
We analyse, develop solutions and implent results.
Should not have
• Typical US-American style elements. We do not want to give the impression of being a US company.

We do not want to appear to be neo-liberal. We are a politically neutral professional consulting firm.

```html
<!DOCTYPE html>
<html lang="en">
<head>
<meta charset="utf-8">
<title>Brevalto Brochure – Investment Management &amp; Finance Solutions</title>
<link rel="stylesheet" href="https://fonts.googleapis.com/css2?family=Source+Sans+3:wght@400;600;700&display=swap">
<style>
  :root {
    --page-bg: #ffffff;
    --band-blue: #5a7bbd;
    --rule-blue: #4f74bf;
    --ink: #111111;
    --paper: #ffffff;
    --fold: #9a9a9a;
    --photo-cool: #dfe6ee;
    --photo-mid: #eeede9;
    --photo-warm: #e6d8c6;
  }
  html, body {
    margin: 0;
    padding: 0;
    width: 1200px;
    height: 900px;
    overflow: hidden;
    background: var(--page-bg);
    font-family: "Source Sans 3", "Helvetica Neue", Arial, sans-serif;
  }
  .canvas {
    position: relative;
    width: 1200px;
    height: 900px;
  }
  .spread {
    position: absolute;
    left: 112px;
    top: 105px;
    width: 976px;
    height: 690px;
    background: var(--paper);
    box-shadow: 0 0 4px rgba(0,0,0,0.18);
    overflow: hidden;
  }
  .band {
    position: absolute;
    left: 0;
    top: 0;
    width: 100%;
    height: 137px;
    background: var(--band-blue);
  }
  .section-title {
    position: absolute;
    top: 86px;
    margin: 0;
    color: #fff;
    font-size: 16.5px;
    font-weight: 600;
    letter-spacing: 0.07em;
    line-height: 21px;
    text-transform: uppercase;
  }
  .section-body {
    position: absolute;
    top: 164px;
    color: var(--ink);
    font-size: 8.6px;
    font-weight: 600;
    line-height: 12.4px;
    white-space: nowrap;
  }
  .section-body p { margin: 0 0 12.4px; }
  .col-left { left: 46px; }
  .col-right { left: 534px; }
  .photo-rule {
    position: absolute;
    left: 0;
    top: 413px;
    width: 100%;
    height: 2px;
    background: var(--rule-blue);
  }
  .photo {
    position: absolute;
    left: 0;
    top: 415px;
    width: 100%;
    height: 275px;
    background: linear-gradient(90deg, var(--photo-cool) 0%, var(--photo-mid) 50%, var(--photo-warm) 100%);
  }
  .fold-line {
    position: absolute;
    left: 599px;
    top: 80px;
    height: 740px;
    border-left: 1px dashed var(--fold);
  }
</style>
</head>
<body>
  <div class="canvas">
    <div class="spread">
      <div class="band"></div>

      <h2 class="section-title col-left">Investment<br>Management</h2>
      <div class="section-body col-left">
        <p>Brevalto has a clear business-like approach to investments.</p>
        <p>We only engage in those projects or companies with which we have a<br>strong relationship.</p>
        <p>That is why we are also willing to take an entrepreneurial risk in the<br>companies we invest in. We participate with our own capital and<br>assume functions in the company’s management.</p>
        <p>Brevalto currently holds shares in seven SMEs; four of these to<br>100%. Participation is on equal terms, and two of the companies we<br>are minority shareholders.</p>
      </div>

      <h2 class="section-title col-right">Finance<br>Solutions</h2>
      <div class="section-body col-right">
        <p>Financing growth opportunities sometimes calls for an<br>entrepreneurial perspective, which is often not found in the<br>traditional banking world.</p>
        <p>That is why we have committed ourselves to developing financing<br>solutions for unconventional requirements. To do so, we often work<br>with partners with complementary subject matter expertise and<br>geographical coverage.</p>
        <p>This gives us the flexibility to create innovative solutions – solutions<br>that meet our clients’ special needs.</p>
      </div>

      <div class="photo-rule"></div>
      <div class="photo" role="img" aria-label="Photo of a consultant presenting an architectural house model to two clients in a bright office"></div>
    </div>
    <div class="fold-line"></div>
  </div>
</body>
</html>
```